Brightleaf Chiropractic 20th Birthday Party

We are a holistic health practice focussing on women's children's health and we need a poster and an invitation to our 20th birthday celebration.

On Sat Nov 24th 12-3pm at BCC

```html
<!DOCTYPE html>
<html lang="en">
<head>
<meta charset="utf-8">
<title>Brightleaf Chiropractic Centre – 20th Birthday Invitation</title>
<link href="https://fonts.googleapis.com/css2?family=Mulish:wght@800&family=Philosopher&family=Yellowtail&display=swap" rel="stylesheet">
<style>
  :root {
    --page-bg: #f3f3f3;
    --card-bg: #ffffff;
    --teal: #4bc3bb;
    --teal-light: #66ccc5;
    --orange: #ef5a24;
    --white: #ffffff;
  }
  html, body {
    margin: 0;
    padding: 0;
    width: 1200px;
    height: 935px;
    overflow: hidden;
    background: var(--page-bg);
  }
  .invitation {
    position: absolute;
    left: 322px;
    top: 107px;
    width: 556px;
    height: 720px;
    background: var(--card-bg);
    overflow: hidden;
  }
  .masthead {
    position: absolute;
    left: 0;
    top: 0;
    width: 100%;
    height: 140px;
    background: var(--teal);
  }
  .brand-tile {
    position: absolute;
    left: 225px;
    top: 0;
    width: 106px;
    height: 91px;
    background: var(--teal-light);
    display: flex;
    align-items: center;
    justify-content: center;
  }
  .brand-name {
    font-family: "Mulish", sans-serif;
    font-weight: 800;
    font-size: 17px;
    color: var(--white);
  }
  .centre-name {
    position: absolute;
    left: 0;
    width: 100%;
    top: 84px;
    margin: 0;
    text-align: center;
    font-family: "Yellowtail", cursive;
    font-weight: 400;
    font-size: 40px;
    line-height: 48px;
    color: var(--white);
  }
  .event-title {
    position: absolute;
    left: 0;
    width: 100%;
    top: 172px;
    margin: 0;
    text-align: center;
    font-family: "Philosopher", sans-serif;
    font-weight: 400;
    font-size: 23px;
    color: var(--orange);
  }
  .content {
    position: absolute;
    left: 64px;
    top: 240px;
    width: 470px;
    font-family: "Mulish", sans-serif;
    font-weight: 800;
  }
  .about {
    margin: 0;
    font-size: 21px;
    line-height: 27px;
    color: var(--teal);
  }
  .details {
    margin: 26px 0 0;
    font-size: 17px;
    line-height: 23px;
    color: var(--orange);
  }
  .details dt { margin: 0; }
  .welcome {
    margin: 20px 0 0;
    font-size: 21px;
    line-height: 27px;
    color: var(--teal);
  }
  .swirl-decoration {
    position: absolute;
    left: 252px;
    top: 484px;
    width: 304px;
    height: 236px;
    background: radial-gradient(ellipse at 70% 60%, rgba(75,195,187,0.35) 0%, rgba(75,195,187,0.15) 50%, rgba(75,195,187,0) 75%);
  }
</style>
</head>
<body>
  <article class="invitation">
    <header class="masthead">
      <div class="brand-tile"><span class="brand-name">Brightleaf</span></div>
      <h1 class="centre-name">Brightleaf Chiropractic Centre</h1>
    </header>

    <h2 class="event-title">Invitation To Our 20th Birthday Celebration</h2>

    <section class="content">
      <p class="about">We provide chiropractic care to children, babies and families throughout Newcastle and Lake Macquarie including Charlestown, Warners Bay, Adamstown and Belmont.</p>
      <dl class="details">
        <dt>Date:</dt>
        <dt>Venue:</dt>
      </dl>
      <p class="welcome">We welcome your family to our family!</p>
    </section>

    <div class="swirl-decoration" role="img" aria-label="Decorative teal swirl circles in the lower right corner"></div>
  </article>
</body>
</html>
```